Capacity building in Resource Management

Need design of a business card (later to be completed by letterhead and webdesign in same fashion) for a professional who works in the field of capacity building of professionals in mostly developing countries in the field waste/resource management, waste prevention/reduction, cleaner production, stakeholders involvement, etc.
Info on business cards is to include provided logo, info in provided file and picture.

Industry/Entity Type

Business

Contact Information for Business Card

White background

Font styles to use
Sans Serif

Colors

Designer to choose colors to be used in the design.

```html
<!DOCTYPE html>
<html lang="en">
<head>
<meta charset="utf-8">
<title>Verdant-Learn business card</title>
<link href="https://fonts.googleapis.com/css2?family=Open+Sans:wght@400;600;700&display=swap" rel="stylesheet">
<style>
  :root {
    --page: #ffffff;
    --card: #f2f2f2;
    --green-dark: #0b4d22;
    --green: #2e7d32;
    --band: #0c5a24;
    --text: #1f3d29;
    --photo-a: #8fa889;
    --photo-b: #6b5a4a;
  }
  * { margin: 0; padding: 0; box-sizing: border-box; }
  html, body { width: 1200px; height: 1200px; overflow: hidden; background: var(--page); }
  body { position: relative; font-family: "Open Sans", sans-serif; }

  .card {
    position: absolute;
    left: 197px;
    width: 840px;
    height: 478px;
    background: var(--card);
    overflow: hidden;
  }
  .card--front { top: 56px; }
  .card--back { top: 656px; }

  .front-brand {
    position: absolute;
    left: 0; right: 0;
    top: 178px;
    text-align: center;
  }
  .front-brand__name {
    font-weight: 700;
    font-size: 64px;
    line-height: 1;
    color: var(--green);
    letter-spacing: 1px;
  }
  .front-brand__tagline {
    margin-top: 14px;
    font-size: 16px;
    color: var(--green-dark);
    letter-spacing: 0.5px;
  }

  .back-art { position: absolute; inset: 0; }

  .identity { position: absolute; left: 50px; top: 96px; color: var(--green-dark); }
  .identity__name { font-weight: 600; font-size: 21px; line-height: 26px; }
  .identity__tagline { font-size: 18px; line-height: 26px; color: var(--text); }

  .address { position: absolute; left: 50px; top: 206px; font-size: 15px; line-height: 20px; color: var(--text); }

  .contacts { position: absolute; left: 50px; top: 282px; list-style: none; }
  .contacts__item { display: flex; align-items: center; height: 27px; font-size: 16px; color: var(--green-dark); }
  .contacts__item--small { font-size: 14px; }
  .contacts__icon { width: 18px; height: 18px; margin-right: 22px; flex: none; }
</style>
</head>
<body>

<section class="card card--front" aria-label="Card front">
  <div class="front-brand">
    <div class="front-brand__name">verdant-learn</div>
    <div class="front-brand__tagline">capacity building in resource management</div>
  </div>
</section>

<section class="card card--back" aria-label="Card back">
  <svg class="back-art" width="840" height="478" viewBox="0 0 840 478">
    <defs>
      <linearGradient id="portrait-tone" x1="0" y1="0" x2="1" y2="1">
        <stop offset="0" stop-color="var(--photo-a)"/>
        <stop offset="0.55" stop-color="var(--photo-b)"/>
        <stop offset="1" stop-color="#d9d6d2"/>
      </linearGradient>
    </defs>
    <rect x="0" y="451" width="620" height="27" fill="var(--band)"/>
    <circle cx="731" cy="248" r="280" fill="url(#portrait-tone)" role="img" aria-label="Portrait photo of the consultant outdoors with greenery behind"/>
  </svg>

  <div class="identity">
    <div class="identity__name">Verdant-Learn</div>
    <div class="identity__tagline">Capacity building in<br>Resource Management</div>
  </div>

  <div class="address">Lindenweg 12<br>10117 Berlin / Germany</div>

  <ul class="contacts">
    <li class="contacts__item">
      <svg class="contacts__icon" viewBox="0 0 18 18"><rect width="18" height="18" fill="var(--green-dark)"/><path d="M4 8c0-2 2-3 5-3s5 1 5 3h-3V7H7v1zM5 9h8l1 5H4z" fill="#fff"/></svg>
      +49 1500 000 1234
    </li>
    <li class="contacts__item">
      <svg class="contacts__icon" viewBox="0 0 18 18"><rect width="18" height="18" fill="var(--green-dark)"/><rect x="3.5" y="5" width="11" height="8" fill="none" stroke="#fff" stroke-width="1.3"/><path d="M3.5 5l5.5 4.5L14.5 5" fill="none" stroke="#fff" stroke-width="1.3"/></svg>
      joris.velden@verdant-learn.com
    </li>
    <li class="contacts__item">
      <svg class="contacts__icon" viewBox="0 0 18 18"><rect width="18" height="18" fill="var(--green-dark)"/><circle cx="9" cy="9" r="5" fill="none" stroke="#fff" stroke-width="1.3"/><path d="M4 9h10M9 4c-2 3-2 7 0 10M9 4c2 3 2 7 0 10" fill="none" stroke="#fff" stroke-width="1"/></svg>
      www.verdant-learn.com
    </li>
    <li class="contacts__item contacts__item--small">
      <svg class="contacts__icon" viewBox="0 0 18 18"><rect width="18" height="18" fill="var(--green-dark)"/></svg>
      @jorisvelden
    </li>
    <li class="contacts__item contacts__item--small">
      <svg class="contacts__icon" viewBox="0 0 18 18"><rect width="18" height="18" fill="var(--green-dark)"/></svg>
      Joris Velden
    </li>
  </ul>
</section>

</body>
</html>
```